Poster Required for Cafe to promote coffee/staff discounts

Need an A3 size poster designed for our business to promote that we roast our own coffee, and that we offer discounts for staff.
I have attached a poster which we use to promote catering that our business offers, also have attached logos and our business card..
Also, I have attached our business card I would like the poster to look a little like that.
Eg. Our logo.
Then Specialty Coffee Roasters (under or next to this, in small print: Producing Slow Roasted Coffee)
Location
Download our App
Website
I would like the poster to state:
Tarrindale Health Staff receive $1 off their coffee or hot drink when presenting their staff pass.
Please don't hesitate to ask if you need more info.

```html
<!DOCTYPE html>
<html lang="en">
<head>
<meta charset="utf-8">
<title>Kettle &amp; Cup – Coffee Poster</title>
<link href="https://fonts.googleapis.com/css2?family=Anton&family=Oswald:wght@400;500&display=swap" rel="stylesheet">
<style>
  :root {
    --backdrop: #e9e6e1;
    --frame: #0d0b0a;
    --burlap-light: #d9b45a;
    --burlap-mid: #bf9038;
    --burlap-dark: #8a6120;
    --ink: #1a1410;
    --badge: #2b2623;
    --badge-text: #f4efe8;
    --pill-text: #f6e58c;
    --band: rgba(244, 222, 140, 0.78);
    --bean-light: #8a5a36;
    --bean-dark: #2e1a0f;
  }
  * { margin: 0; padding: 0; box-sizing: border-box; }
  html, body {
    width: 935px;
    height: 1200px;
    overflow: hidden;
    background: var(--backdrop);
  }
  .poster {
    position: absolute;
    left: 98px;
    top: 130px;
    width: 714px;
    height: 1008px;
    background: var(--frame);
    padding: 15px;
  }
  .poster__surface {
    position: relative;
    width: 100%;
    height: 100%;
    overflow: hidden;
    background:
      radial-gradient(ellipse at 50% 35%, var(--burlap-light) 0%, var(--burlap-mid) 55%, var(--burlap-dark) 100%);
  }
  .brand-badge {
    position: absolute;
    left: 170px;
    top: 28px;
    width: 344px;
    height: 344px;
    border-radius: 50%;
    background: var(--badge);
    display: flex;
    flex-direction: column;
    align-items: center;
    justify-content: center;
    padding-bottom: 30px;
  }
  .brand-badge__name {
    font-family: "Oswald", sans-serif;
    font-weight: 400;
    color: var(--badge-text);
    font-size: 44px;
    letter-spacing: 6px;
    line-height: 1.1;
    text-align: center;
  }
  .tagline {
    position: absolute;
    z-index: 2;
    left: 0;
    width: 100%;
    top: 390px;
    text-align: center;
    font-family: "Oswald", sans-serif;
    font-weight: 400;
    font-size: 15px;
    color: var(--ink);
  }
  .beans-photo {
    position: absolute;
    z-index: 1;
    left: 187px;
    top: 310px;
    width: 497px;
    height: 185px;
    background: linear-gradient(100deg, var(--bean-light) 0%, var(--bean-dark) 70%);
    clip-path: polygon(0 70%, 50% 64%, 58% 60%, 70% 30%, 85% 12%, 100% 0, 100% 100%, 0 100%);
  }
  .location {
    position: absolute;
    left: 0;
    width: 100%;
    top: 505px;
    text-align: center;
    font-family: "Oswald", sans-serif;
    color: var(--ink);
    line-height: 1.3;
  }
  .location__place { font-size: 23px; font-weight: 400; }
  .location__region { font-size: 22px; font-weight: 500; letter-spacing: 0.5px; }
  .app-pill {
    position: absolute;
    left: 204px;
    top: 701px;
    width: 275px;
    height: 44px;
    border-radius: 22px;
    background: var(--ink);
    color: var(--pill-text);
    font-family: "Anton", sans-serif;
    font-size: 24px;
    letter-spacing: 0.5px;
    display: flex;
    align-items: center;
    justify-content: center;
  }
  .website {
    position: absolute;
    left: 0;
    width: 100%;
    top: 772px;
    text-align: center;
    font-family: "Oswald", sans-serif;
    font-size: 18px;
    color: var(--ink);
  }
  .offer-band {
    position: absolute;
    left: 0;
    width: 100%;
    top: 855px;
    height: 68px;
    background: var(--band);
    display: flex;
    align-items: center;
    justify-content: center;
    text-align: center;
    font-family: "Anton", sans-serif;
    font-size: 21px;
    line-height: 1.25;
    color: var(--ink);
    letter-spacing: 0.2px;
  }
  .base-band {
    position: absolute;
    left: 0;
    width: 100%;
    top: 923px;
    bottom: 0;
    background: rgba(110, 74, 22, 0.35);
  }
</style>
</head>
<body>
  <main class="poster">
    <div class="poster__surface">
      <div class="brand-badge">
        <p class="brand-badge__name">KETTLE &amp;<br>CUP</p>
      </div>
      <p class="tagline">Producing Slow Roasted Coffee</p>
      <div class="beans-photo" role="img" aria-label="Photograph of roasted coffee beans spread across the poster"></div>
      <div class="location">
        <p class="location__place">Located at Marlowe Hospital</p>
        <p class="location__region">QUEENSLAND, AUSTRALIA</p>
      </div>
      <div class="app-pill">DOWNLOAD OUR APP</div>
      <p class="website">kettleandcup.com.au</p>
      <div class="offer-band">
        <p>TARRINDALE HEALTH STAFF RECEIVE $1 OFF THEIR COFFEE OR<br>HOT DRINK WHEN PRESENTING THEIR STAFF PASS.</p>
      </div>
      <div class="base-band"></div>
    </div>
  </main>
</body>
</html>
```